Private School Website Revamp

We need a new design for the private school's website revamp. The new website will be using WordPress CMS, but we will be using it to handle custom data types, not blogs - so the content will not be typical blog-style.

The school has indicated the following template which they like, and our design to follow the design style.
http://qrv7.layoutkiosk-demo.com/sitekit_48215/
However, follow the school's colour-theme and sitemap.

Colour-theme: White, Green (refer to current website - www.morvelan.com.sg)

Sitemap: (for navigation menu)
- Home
- Academic & Examination Board
- Our Philosophy
- Our Programmes
+ Preparatory Courses
+ Tuition Classes
+ Study Tours
- Our Hostel
- Trial Tests
+ English
+ Mathematics
- Contact Us

Target Market(s)

Parents looking for private school services.
Existing students of the private school accessing trial tests.

Industry/Entity Type

School

Requirements
Must have
• Homepage design to include
• - Logo, navigation menu, search box
• - Featured area/slideshow (see prefered template above)
• - Section for Preparatory Courses
• - Section for Tuition Classes
• - Section for Study Tours
• - Section for Hostel Stay
• - Awards & Certification box
• - Footer contact details
Nice to have
• - Pictures of happy students
• - The Message from Director box is "nice to have", but no necessary if it does not fit into homepage design.

```html
<!DOCTYPE html>
<html lang="en">
<head>
<meta charset="utf-8">
<title>Morvelan Private School</title>
<link rel="stylesheet" href="https://fonts.googleapis.com/css2?family=Arimo:wght@400;700&family=Roboto:wght@300;400&family=Bubblegum+Sans&display=swap">
<style>
:root{
  --sky-top:#3f8fd0;
  --sky-mid:#7fb8e4;
  --sky-low:#bcdcf3;
  --green-dark:#0d4a10;
  --green:#1f6d1b;
  --green-light:#2f8a28;
  --yellow:#f3e81d;
  --orange:#f29a3a;
  --ink:#1b1b1b;
  --panel:#ffffff;
  --panel-fade:#dcdcdc;
  --border:#9aa3ab;
  --btn:#4d4d4d;
  --footer:#1c1c1c;
  --footer-text:#d8d8d8;
}
*{box-sizing:border-box;margin:0;padding:0}
html,body{width:1200px;height:1040px;overflow:hidden}
body{
  position:relative;
  font-family:"Arimo",Arial,sans-serif;
  color:var(--ink);
  background:linear-gradient(180deg,var(--sky-top) 0px,var(--sky-mid) 520px,var(--sky-low) 880px,var(--sky-low) 921px);
}
.abs{position:absolute}
a{text-decoration:none}

/* search */
.search{left:813px;top:7px;width:200px;height:23px;display:flex;border-radius:3px;overflow:hidden}
.search input{flex:1 1 auto;min-width:0;width:0;border:0;background:#fff;font:13px "Arimo",sans-serif;padding:0 7px;color:#222}
.search button{flex:0 0 34px;width:34px;border:0;background:var(--green-dark);color:#fff;font:bold 13px "Arimo",sans-serif;padding:0}

/* brand */
.brand{left:177px;top:36px;height:62px;display:flex;align-items:center;gap:10px;white-space:nowrap}
.brand-mark{width:22px;height:22px;background:var(--green-dark);border-radius:50%;flex:0 0 22px}
.brand-name{font:700 16px "Arimo",sans-serif;color:var(--green-dark);letter-spacing:.5px}

/* nav */
.nav{left:171px;top:115px;width:842px;height:27px;border:1px solid #8d949a;border-radius:4px;
  background:linear-gradient(#f7f7f7,#cfcfcf);display:flex;justify-content:space-around;align-items:center;padding:0 8px}
.nav a{font:14px "Arimo",sans-serif;color:#222;transform:scaleX(.92);white-space:nowrap}

/* panels */
.panel{background:linear-gradient(180deg,var(--panel) 40%,var(--panel-fade));border:1px solid var(--border);border-radius:8px;overflow:hidden}
.btn{display:inline-flex;align-items:center;background:var(--btn);color:#e6e6e6;border-radius:3px;font:17px "Roboto",sans-serif;padding:0 0 0 7px;height:28px;white-space:nowrap}
.btn i{margin-left:6px;width:20px;height:28px;background:#6f6f6f;display:flex;align-items:center;justify-content:center;border-radius:0 3px 3px 0}
.btn i svg{width:10px;height:12px}

/* hero */
.hero{left:171px;top:148px;width:842px;height:255px;background:#fff}
.hero h1{position:absolute;left:24px;top:14px;font:300 43px "Roboto",sans-serif;color:var(--orange);white-space:nowrap}
.hero p{position:absolute;left:26px;top:80px;width:162px;font:11.5px/12.7px "Arimo",sans-serif;color:#222}
.hero .btn{position:absolute;left:26px;top:200px;height:30px;font-size:19px}
.hero .btn i{height:30px}
.hero-photo{position:absolute;left:214px;top:0;width:628px;height:255px;
  background:linear-gradient(180deg,#d9dde2 0%,#c3c8cf 45%,#8e949c 100%)}

/* feature cards */
.card{top:415px;width:199px;height:205px}
.card-title{position:absolute;left:9px;top:9px;width:180px;height:40px;border-radius:4px;
  background:linear-gradient(var(--green-light),var(--green-dark));display:flex;align-items:center;justify-content:center;
  font:19px "Bubblegum Sans",cursive;color:var(--yellow);font-variant:small-caps;letter-spacing:.5px;white-space:nowrap}
.card h3{position:absolute;left:11px;top:60px;font:700 11.5px "Arimo",sans-serif;white-space:nowrap}
.card p{position:absolute;left:11px;top:86px;width:178px;font:11.5px/13px "Arimo",sans-serif;color:#222}
.card .btn{position:absolute;left:46px;top:170px;height:24px;font-size:15px}
.card .btn i{height:24px}

/* hostel */
.hostel{left:171px;top:637px;width:412px;height:216px}
.hostel-side{position:absolute;left:0;top:0;width:155px;height:216px;background:linear-gradient(var(--green),var(--green-dark));color:#fff;padding:8px 14px}
.hostel-side h2{font:22px "Bubblegum Sans",cursive;color:var(--yellow);font-variant:small-caps;letter-spacing:.5px;white-space:nowrap}
.hostel-side h3{margin-top:10px;font:700 11.5px/1.2 "Arimo",sans-serif}
.hostel-side p{margin-top:14px;font:11.5px/13px "Arimo",sans-serif}
.hostel-map{position:absolute;left:155px;top:0;width:257px;height:216px;background:linear-gradient(135deg,#e8e6e0,#d7d4cc)}

/* director */
.director{left:601px;top:637px;width:412px;height:216px}
.director h2{position:absolute;left:8px;top:6px;font:400 18px "Roboto",sans-serif;color:#222;white-space:nowrap}
.director p{position:absolute;left:10px;top:35px;width:236px;font:11px/12.6px "Arimo",sans-serif;color:#333}
.director-photo{position:absolute;left:255px;top:13px;width:146px;height:186px;border:3px solid #111;
  background:linear-gradient(180deg,#b8c0c8,#4a4f57)}

/* footer */
.footer{left:0;top:921px;width:1200px;height:119px;background:var(--footer);color:var(--footer-text);font:11.5px/13px "Arimo",sans-serif}
.footer address{position:absolute;left:173px;top:8px;font-style:normal}
.footer small{position:absolute;right:187px;top:8px;font-size:11px;white-space:nowrap}
</style>
</head>
<body>

<form class="search abs"><input type="text" value="seach" aria-label="Search"><button type="button">go</button></form>

<div class="brand abs"><span class="brand-mark"></span><span class="brand-name">MORVELAN PRIVATE SCHOOL</span></div>

<nav class="nav abs">
  <a href="#">Home</a><a href="#">Academic &amp; Examination Board</a><a href="#">Our Philosophy</a>
  <a href="#">Our Programmes</a><a href="#">Our Hostel</a><a href="#">Trial Tests</a><a href="#">Contact Us</a>
</nav>

<section class="hero panel abs">
  <h1>Headline</h1>
  <p>Lorem ipsum dolor sit amet, consectetur adipisicing elit, sed do eiusmod tempor incididunt ut labore et dolore magna aliqua. Ut enim ad minim veniam, quis nostrud exercitation ullamco laboris nisi ut aliquip ex ea commodo consequat. Duis aute</p>
  <a class="btn" href="#">Read more<i><svg viewBox="0 0 10 12"><path d="M1 0l9 6-9 6z" fill="#bbb"/></svg></i></a>
  <div class="hero-photo" role="img" aria-label="Group of smiling students holding colourful folders"></div>
</section>

<section class="card panel abs" style="left:171px">
  <div class="card-title">Preparatory Courses</div>
  <h3>Nulla dui. Fusce feuaada ore.</h3>
  <p>Mauris fermentum dictum gna. Sedaoreet aliquam leo. Ut Mauris fermentum dictum gna. Sedaoreet aliquam leo. Ut Mauris fermentum dictum gna. Sedaoreet aliquam leo. Ut</p>
  <a class="btn" href="#">Read more<i><svg viewBox="0 0 10 12"><path d="M1 0l9 6-9 6z" fill="#bbb"/></svg></i></a>
</section>
<section class="card panel abs" style="left:385px">
  <div class="card-title">Tuition Classes</div>
  <h3>Nulla dui. Fusce feuaada ore.</h3>
  <p>Mauris fermentum dictum gna. Sedaoreet aliquam leo. Ut Mauris fermentum dictum gna. Sedaoreet aliquam leo. Ut Mauris fermentum dictum gna. Sedaoreet aliquam leo. Ut</p>
  <a class="btn" href="#">Read more<i><svg viewBox="0 0 10 12"><path d="M1 0l9 6-9 6z" fill="#bbb"/></svg></i></a>
</section>
<section class="card panel abs" style="left:600px">
  <div class="card-title">Study Tours</div>
  <h3>Nulla dui. Fusce feuaada ore.</h3>
  <p>Mauris fermentum dictum gna. Sedaoreet aliquam leo. Ut Mauris fermentum dictum gna. Sedaoreet aliquam leo. Ut Mauris fermentum dictum gna. Sedaoreet aliquam leo. Ut</p>
  <a class="btn" href="#">Read more<i><svg viewBox="0 0 10 12"><path d="M1 0l9 6-9 6z" fill="#bbb"/></svg></i></a>
</section>
<section class="card panel abs" style="left:815px">
  <div class="card-title">Awards &amp; Certification</div>
  <h3>Nulla dui. Fusce feuaada ore.</h3>
  <p>Mauris fermentum dictum gna. Sedaoreet aliquam leo. Ut Mauris fermentum dictum gna. Sedaoreet aliquam leo. Ut Mauris fermentum dictum gna. Sedaoreet aliquam leo. Ut</p>
  <a class="btn" href="#">Read more<i><svg viewBox="0 0 10 12"><path d="M1 0l9 6-9 6z" fill="#bbb"/></svg></i></a>
</section>

<section class="hostel panel abs">
  <div class="hostel-side">
    <h2>Hostel Stay</h2>
    <h3>Nulla dui. Fusce<br>feuaada ore.</h3>
    <p>Mauris fermentum dictum gna. Sedaoreet aliquam leo. Ut Mauris fermentum dictum gna. Sedaoreet aliquam leo. Ut Mauris fermentum dictum gna. Sedaoreet aliquam leo. Ut</p>
  </div>
  <div class="hostel-map" role="img" aria-label="Street map showing the hostel location"></div>
</section>

<section class="director panel abs">
  <h2>Message from Director</h2>
  <p>Morvelan Private School was founded to meet the growing demand of foreign students seeking an effective bilingual education in Singapore.<br><br>We are managed by a group of professionals who are formerly Ministry of Education senior officers and we have a team of dedicated.<br><br>Yours sincerely,<br>Mr Lim Wei Han<br>Director<br>Morvelan Private School</p>
  <div class="director-photo" role="img" aria-label="Portrait photo of the school director"></div>
</section>

<footer class="footer abs">
  <address>14 Pelham Grove St 31<br>Larkfield Community Hall, #02-05<br>S(604417)<br><br>Tel: +65 6100 2384<br>Fax: +65 6100 2391<br>Email: school@morvelan.com.sg</address>
  <small>© 2008. MORVELAN PRIVATE SCHOOL. ALL RIGHTS RESERVED</small>
</footer>

</body>
</html>
```